Family-owned company selling organic landscaping and gardening products needs new labels.

We need label designs initially for 6 products, the designs should be unique for each product but have common design elements. The products are organic and used in landscaping, gardening and horticulture industries. Products are used commercially and residentially. The products encourage root growth and soil health, so that could be featured in the label along with plants, trees, etc. We like the colors, the sunburst background and the art deco vibe in the label designs provided for inspiration, but we are open to other ideas as well. We are also providing a sample of current labels (bland, boring) for reference. We are also providing a copy of our new logo which we like but are open to suggestions. We would like to start with the label for our QUILO DEX product.

```html
<!DOCTYPE html>
<html lang="en">
<head>
<meta charset="utf-8">
<title>QUILO DEX Label</title>
<link href="https://fonts.googleapis.com/css2?family=Days+One&family=Baloo+2:wght@600;700;800&display=swap" rel="stylesheet">
<style>
  :root {
    --page-bg: #ececec;
    --red-core: #e0202f;
    --red-mid: #b8162a;
    --red-deep: #8e1020;
    --red-dark: #6a0f1c;
    --plant-tone: #5a0a16;
    --ink: #111111;
    --white: #ffffff;
    --pink-text: #ffd6dc;
    --title-shadow: #9a9a9a;
  }
  * { margin: 0; padding: 0; box-sizing: border-box; }
  html, body { width: 1088px; height: 1200px; overflow: hidden; background: var(--page-bg); }
  .canvas { position: relative; width: 1088px; height: 1200px; }

  .label {
    position: absolute; left: 104px; top: 65px; width: 880px; height: 1070px;
    overflow: hidden;
    background: radial-gradient(circle at 50% 40%, var(--red-core) 0%, var(--red-mid) 45%, var(--red-deep) 85%);
  }
  .sunburst { position: absolute; inset: 0; }

  .title {
    position: absolute; left: 0; right: 0; top: 40px;
    font-family: "Days One", sans-serif; color: var(--white);
    font-size: 190px; line-height: 0.98; text-align: center; letter-spacing: 4px;
    text-shadow: 4px 5px 0 var(--title-shadow), 8px 10px 0 rgba(0,0,0,0.25);
  }

  .pill {
    position: absolute; left: 100px; right: 100px; top: 455px; height: 128px;
    background: var(--ink); border-radius: 64px;
    display: flex; flex-direction: column; justify-content: center; align-items: center;
    font-family: "Baloo 2", sans-serif; font-weight: 700; color: var(--white);
    font-size: 38px; line-height: 1.15;
  }

  .classification {
    position: absolute; left: 0; right: 0; top: 600px; text-align: center;
    font-family: "Baloo 2", sans-serif; font-weight: 800; color: var(--pink-text);
    font-size: 30px; line-height: 1.1; text-transform: uppercase; letter-spacing: 1px;
  }

  .plant-art {
    position: absolute; left: 0; right: 0; top: 680px; height: 200px;
    background: linear-gradient(180deg,
      rgba(90,10,22,0) 0%,
      rgba(90,10,22,0.45) 35%,
      rgba(90,10,22,0.7) 70%,
      var(--plant-tone) 100%);
  }

  .hills { position: absolute; left: 0; right: 0; bottom: 0; height: 250px; }

  .brand {
    position: absolute; left: 80px; bottom: 70px; width: 170px; height: 170px;
    border-radius: 50%; background: var(--white); border: 6px solid var(--ink);
    display: flex; align-items: center; justify-content: center;
    font-family: "Baloo 2", sans-serif; font-weight: 800; color: var(--ink); font-size: 38px;
  }

  .net-contents {
    position: absolute; left: 290px; bottom: 115px;
    font-family: "Baloo 2", sans-serif; font-weight: 700; color: var(--white);
    font-size: 32px; line-height: 1.3;
  }
</style>
</head>
<body>
<div class="canvas">
  <div class="label">
    <svg class="sunburst" viewBox="0 0 880 1070" aria-hidden="true">
      <g fill="none" stroke="rgba(255,255,255,0.06)" stroke-width="30">
        <circle cx="440" cy="430" r="90"/>
        <circle cx="440" cy="430" r="190"/>
        <circle cx="440" cy="430" r="300"/>
        <circle cx="440" cy="430" r="420"/>
        <circle cx="440" cy="430" r="550"/>
      </g>
    </svg>

    <h1 class="title">QUILO<br>DEX</h1>

    <div class="pill">
      <span>Endo-Ecto Mycorrhizal Inoculum</span>
      <span>For Most Plants</span>
    </div>

    <p class="classification">Auxiliary soil and plant substance<br>Non plant food ingredient</p>

    <div class="plant-art" role="img" aria-label="Line drawing of wildflowers, herbs and grasses growing along the hills"></div>

    <svg class="hills" viewBox="0 0 880 250" preserveAspectRatio="none" aria-hidden="true">
      <defs>
        <linearGradient id="hillFade" x1="0" y1="0" x2="0" y2="1">
          <stop offset="0" stop-color="#7a1220"/>
          <stop offset="1" stop-color="#5a0c16"/>
        </linearGradient>
      </defs>
      <path d="M0 60 C150 20 300 50 430 35 C560 20 700 45 880 10 L880 250 L0 250 Z" fill="url(#hillFade)"/>
      <path d="M0 120 C200 80 380 125 560 90 C700 65 800 80 880 72 L880 250 L0 250 Z" fill="rgba(60,5,12,0.35)"/>
    </svg>

    <div class="brand">Terrow</div>

    <div class="net-contents">
      <div>500 – 4 gram Quilo Dex Paks</div>
      <div>Net Weight: 4.41 lbs (2.0 kg)</div>
    </div>
  </div>
</div>
</body>
</html>
```